Business Cards for Marco and Tobin

Design of business cards for two people with the recently created brand Valcor Mobile. Valcor Mobile wants to become a worldwide major player on the secondhand phone market. It gathers send hand phones from individuals, refurbish them and sell them throughout the world. It has a green impact (recycling) and we also contribute to social project in Africa (a percentage of our benefits are sent to build school, sport facilities, etc.

Target Market(s)

B2B - Marco and Tobin are in contact with distributors across Africa.

Industry/Entity Type

Wireless Communication

Contact Information for Business Card

Marco Feuillet
Head of Emerging Markets
Valcor Energy South Africa (Pty) Ltd
Kestrel Road 47
2031 Sandton - Johannesburg
South Africa
Tel: + 27 10 555 0148
Mobile : +27 82 55 104
Email : marco.feuillet@valcormobile.example
Skype: marco.feuillet
Web: www.valcormobile.example
 

Tobin Farrow
Head of Southern Africa
Kestrel Road 47
South Africa
Tel: + 27 10 555 0148
Mobile: +27 83 555 0276
Email: tobin.farrow@valcormobile.example
Skype: tobin.farrow
Web: www.valcormobile.example

Requirements
Must have
• The cards need to be "serious", trustable, with a worldwide presence.
Nice to have
• Some "green" / recycling touch would be nice but not necessary if in contradiction with the general design.

```html
<!DOCTYPE html>
<html lang="en">
<head>
<meta charset="utf-8">
<title>Valcor Mobile – Business Card</title>
<link rel="stylesheet" href="https://fonts.googleapis.com/css2?family=Open+Sans:wght@300;700&family=PT+Sans+Narrow:wght@400;700&display=swap">
<style>
  :root {
    --bg: #d8d5d0;
    --navy: #0c2a45;
    --brand-blue: #1c86c8;
    --stripe-blue: #1d5f97;
    --paper: #ecedee;
    --white: #ffffff;
  }
  * { box-sizing: border-box; margin: 0; padding: 0; }
  html, body { width: 1200px; height: 842px; overflow: hidden; }
  body {
    background: var(--bg);
    display: flex;
    align-items: center;
    justify-content: center;
    gap: 40px;
  }
  .card {
    position: relative;
    width: 540px;
    height: 310px;
    overflow: hidden;
    box-shadow: 0 6px 18px rgba(0,0,0,0.18);
  }

  /* Front */
  .card--front { background: var(--paper); }
  .wave-field {
    position: absolute; inset: 0;
    background: linear-gradient(170deg, rgba(236,237,238,1) 0%, rgba(236,237,238,0.4) 40%, rgba(191,227,220,0.7) 70%, rgba(95,191,176,0.55) 100%);
  }
  .brand {
    position: absolute;
    display: flex;
    align-items: center;
    gap: 10px;
    font-family: "Open Sans", sans-serif;
    font-weight: 700;
    white-space: nowrap;
  }
  .brand__dot {
    width: 16px; height: 16px; border-radius: 50%;
    background: var(--brand-blue);
  }
  .card--front .brand {
    left: 50%; top: 50%;
    transform: translate(-50%, -50%);
    font-size: 30px;
    color: var(--navy);
  }

  /* Back */
  .card--back { background: var(--navy); color: var(--white); }
  .edge-stripes {
    position: absolute;
    right: 0; top: 0; bottom: 0;
    width: 110px;
    background: linear-gradient(100deg, rgba(12,42,69,0) 0%, rgba(29,95,151,0.55) 55%, rgba(29,95,151,0.9) 100%);
  }
  .brand-block {
    position: absolute;
    left: 28px; bottom: 34px;
  }
  .card--back .brand {
    position: static;
    font-size: 25px;
    color: var(--white);
  }
  .brand__url {
    font-family: "Open Sans", sans-serif;
    font-weight: 300;
    font-size: 12.5px;
    color: var(--white);
    margin-top: 2px;
    padding-left: 26px;
  }
  .contact {
    position: absolute;
    left: 245px; top: 40px;
    font-family: "PT Sans Narrow", sans-serif;
    font-size: 13.5px;
    line-height: 1.3;
    color: var(--white);
  }
  .contact__name {
    font-family: "Open Sans", sans-serif;
    font-size: 27px;
    line-height: 1.05;
    letter-spacing: 0.5px;
  }
  .contact__name .first { font-weight: 300; }
  .contact__name .last { font-weight: 700; }
  .contact__role {
    font-weight: 700;
    font-size: 19px;
    margin-bottom: 4px;
  }
  .contact__group + .contact__group { margin-top: 10px; }
</style>
</head>
<body>

  <section class="card card--front" aria-label="Business card front">
    <div class="wave-field" role="img" aria-label="Flowing teal wave-line pattern across a light grey card"></div>
    <div class="brand"><span class="brand__dot"></span>Valcor Mobile</div>
  </section>

  <section class="card card--back" aria-label="Business card back">
    <div class="edge-stripes" role="img" aria-label="Diagonal blue stripe pattern along the right edge"></div>

    <div class="contact">
      <div class="contact__name"><span class="first">TOBIN</span> <span class="last">FARROW</span></div>
      <div class="contact__role">Head of Southern Africa</div>
      <div class="contact__group">
        Valcor Energy South Africa (Pty) Ltd<br>
        Kestrel Road 47<br>
        4180 Ridgeview - Kestrel Bay, South Africa
      </div>
      <div class="contact__group">
        Tel: + 27 10 555 0148<br>
        Mobile: + 27 83 555 0276
      </div>
      <div class="contact__group">
        Email: tobin.farrow@valcormobile.example<br>
        Skype: tobin.farrow
      </div>
    </div>

    <div class="brand-block">
      <div class="brand"><span class="brand__dot"></span>Valcor Mobile</div>
      <div class="brand__url">www.valcormobile.example</div>
    </div>
  </section>

</body>
</html>
```